Designer Needed for Protein Label

We are looking for an experienced graphic designer to create a label for our protein supplement Plinth PUREFORM 100% WHEY Protein 3LB tub. You can make it unique to our design but keep it clean and simple.

Here are some design examples that we liked, however please note ours is unflavored:

https://www.shopvarnel.example/BrawnLabs-Vektor-Protein-Powder-Chocolate/dp/Q07RTKZLWA/ref=sr_1_17_a_it?ie=UTF8&qid=1536255229&sr=8-17&keywords=protein%2Bpowder&th=1

https://www.shopvarnel.example/dp/Q093TLMNPX/ref=sspa_dk_detail_1?pd_rd_i=Q093TLMNPX&pf_rd_m=ZQWTYRUVN4KLM&pf_rd_p=7c4410ab-816e-4a2b-c1e7-26e4c2a0167e&pf_rd_r=HRYQLWMNT8KPRD613KJN&pd_rd_wg=KTq4h&pf_rd_s=desktop-dp-sims&pf_rd_t=40701&pd_rd_w=MQRT4&pf_rd_i=desktop-dp-sims&pd_rd_r=339f8965-c2ac-22f9-972d-de17fb2241c2&th=1

Please see attachment for Plinth Logo and additional label example.

Label Dimensions:
18in x 6in

Please include the following information on the label:
* Plinth Icon
* PUREFORM - product name
* 100% WHEY Protein
* Unflavored
* Net WT. 3LB (1.36 KG)
* 40 Servings
* 50 Grams of Protein per serving
* XX  BCAA
* Gluten & Lactose Free
* Kosher and Halal Certified
* Non GMO
* Nutrition Facts (use as place holder)
* Ingredients
* Directions
* Barcode

```html
<!DOCTYPE html>
<html lang="en">
<head>
<meta charset="utf-8">
<title>Plinth PUREFORM 100% Whey Protein – Tub Label</title>
<link rel="stylesheet" href="https://fonts.googleapis.com/css2?family=Bebas+Neue&family=Oswald:wght@200;300;400&family=Roboto+Condensed:wght@400;700&family=Archivo+Black&display=swap">
<style>
  :root {
    --page: #ffffff;
    --label: #404041;
    --yellow: #f6d31a;
    --white: #ffffff;
    --ink: #111111;
  }
  * { margin: 0; padding: 0; box-sizing: border-box; }
  html, body { width: 1200px; height: 468px; overflow: hidden; background: var(--page); }
  body { position: relative; font-family: "Roboto Condensed", sans-serif; }

  .label {
    position: absolute; left: 88px; top: 64px;
    width: 1028px; height: 340px;
    background: var(--label); color: var(--white);
  }
  .label-art { position: absolute; left: 0; top: 0; width: 1028px; height: 340px; overflow: hidden; }
  .abs { position: absolute; }

  .bebas { font-family: "Bebas Neue", sans-serif; fill: var(--white); }
  .oswald-thin { font-family: "Oswald", sans-serif; font-weight: 200; }
  .oswald-light { font-family: "Oswald", sans-serif; font-weight: 300; }
  .fill-yellow { fill: var(--yellow); }
  .fill-white { fill: var(--white); }
  .badge-ring { fill: none; stroke: var(--yellow); stroke-width: 2.2; }
  .badge-name { font-family: "Roboto Condensed", sans-serif; font-size: 7px; fill: var(--yellow); }
  .barcode-slot { fill: var(--yellow); }
  .barcode-note { font-family: "Roboto Condensed", sans-serif; font-weight: 700; font-style: italic; font-size: 9px; fill: var(--label); letter-spacing: .5px; }
  .brand-name { font-family: "Bebas Neue", sans-serif; font-size: 74px; fill: var(--yellow); letter-spacing: 2px; }
  .brand-flavor { font-family: "Bebas Neue", sans-serif; font-size: 22px; fill: var(--yellow); letter-spacing: 3px; }

  .intro-title { left: 36px; top: 196px; font-size: 10px; font-weight: 700; }
  .intro-copy { left: 36px; top: 209px; width: 274px; font-size: 6.4px; line-height: 1.35; }

  /* nutrition panel */
  .facts { left: 718px; top: 24px; width: 162px; height: 168px; background: var(--white); color: var(--ink); padding: 3px 4px; font-size: 3.8px; line-height: 1.25; }
  .facts h2 { font-family: "Archivo Black", sans-serif; font-size: 14.5px; line-height: 1; font-weight: 400; border-bottom: 1px solid var(--ink); padding-bottom: 1px; white-space: nowrap; }
  .facts .thick { border-bottom: 3px solid var(--ink); }
  .facts .thin { border-bottom: .5px solid var(--ink); }
  .facts .row { display: flex; justify-content: space-between; }
  .facts .cols { display: flex; gap: 6px; }
  .facts .cols > div { flex: 1; }
  .facts .grid { display: grid; grid-template-columns: repeat(3, 1fr); column-gap: 6px; padding: 1px 0; }
  .facts .grid span { display: flex; justify-content: space-between; border-bottom: .4px solid #999; }

  .ingredients-side { left: 890px; top: 20px; width: 100px; font-size: 6.4px; line-height: 1.4; }
  .ingredients-side strong { font-size: 9.5px; font-weight: 400; }

  .info { left: 728px; width: 280px; font-size: 6.5px; line-height: 1.42; }
  .info strong { font-size: 7.6px; font-weight: 400; }
  .info.lead { font-size: 7.6px; }
  .info-ingredients { top: 213px; }
  .info-contains { top: 241px; }
  .info-maker { top: 253px; }
  .info-storage { top: 282px; }
  .info-origin { top: 296px; width: 240px; }
</style>
</head>
<body>
<div class="label">

  <svg class="label-art" viewBox="0 0 1028 340" aria-hidden="false">
    <!-- claims stack -->
    <g class="claims">
      <text class="bebas" x="36" y="52" font-size="46" textLength="26" lengthAdjust="spacingAndGlyphs">50</text>
      <text class="bebas" x="37" y="62" font-size="9.5" textLength="24" lengthAdjust="spacingAndGlyphs">GRAMS</text>
      <text class="bebas" transform="translate(62 132) rotate(-90)" font-size="34" textLength="66" lengthAdjust="spacingAndGlyphs">PROTEIN</text>
      <text class="bebas" x="36" y="152" font-size="23" textLength="26" lengthAdjust="spacingAndGlyphs">PER</text>
      <text class="bebas" x="36" y="162" font-size="10" textLength="26" lengthAdjust="spacingAndGlyphs">SERVING</text>

      <text class="bebas" x="68" y="50" font-size="43" textLength="136" lengthAdjust="spacingAndGlyphs">100%WHEY</text>
      <text class="bebas" x="208" y="34" font-size="20" textLength="48" lengthAdjust="spacingAndGlyphs">PROTEIN</text>
      <text class="bebas" x="208" y="50" font-size="20" textLength="48" lengthAdjust="spacingAndGlyphs">PUREFORM</text>

      <text class="bebas" x="68" y="76" font-size="26" textLength="128" lengthAdjust="spacingAndGlyphs">10,900 MG BCAA'S</text>
      <text class="bebas" x="199" y="67" font-size="11" textLength="20" lengthAdjust="spacingAndGlyphs">PER</text>
      <text class="bebas" x="199" y="75" font-size="8" textLength="20" lengthAdjust="spacingAndGlyphs">SERVING</text>

      <text class="bebas" x="68" y="100" font-size="26" textLength="128" lengthAdjust="spacingAndGlyphs">4.6G L-GLUTAMINE</text>
      <text class="bebas" x="199" y="91" font-size="11" textLength="20" lengthAdjust="spacingAndGlyphs">PER</text>
      <text class="bebas" x="199" y="99" font-size="8" textLength="20" lengthAdjust="spacingAndGlyphs">SERVING</text>

      <text class="bebas" transform="translate(258 166) rotate(-90)" font-size="37" textLength="110" lengthAdjust="spacingAndGlyphs">INSTANTIZED</text>

      <text class="bebas" x="68" y="126" font-size="23" textLength="56" lengthAdjust="spacingAndGlyphs">GLUTEN</text>
      <text class="bebas" x="68" y="143" font-size="23" textLength="56" lengthAdjust="spacingAndGlyphs">LACTOSE</text>
      <text class="bebas" x="68" y="160" font-size="23" textLength="58" lengthAdjust="spacingAndGlyphs">ASPARTAME</text>
      <text class="bebas" x="129" y="160" font-size="71" textLength="99" lengthAdjust="spacingAndGlyphs">FREE</text>

      <text class="bebas" x="36" y="186" font-size="23" textLength="222" lengthAdjust="spacingAndGlyphs">WE'RE ALL MORE THAN MUSCLE</text>
    </g>

    <!-- certification badges -->
    <g class="badges">
      <circle class="badge-ring" cx="50" cy="249" r="12.5"/>
      <circle class="badge-ring" cx="98" cy="249" r="12.5"/>
      <circle class="badge-ring" cx="148" cy="249" r="12.5"/>
      <circle class="badge-ring" cx="204" cy="249" r="12.5"/>
      <circle class="badge-ring" cx="252" cy="249" r="12.5"/>
      <text class="badge-name" x="50" y="270" text-anchor="middle">Gluten Free</text>
      <text class="badge-name" x="98" y="270" text-anchor="middle">Lactose Free</text>
      <text class="badge-name" x="148" y="270" text-anchor="middle">Kosher Certified</text>
      <text class="badge-name" x="204" y="270" text-anchor="middle">Halal Certified</text>
      <text class="badge-name" x="252" y="270" text-anchor="middle">Non GMO</text>
    </g>

    <!-- barcode placement -->
    <rect class="barcode-slot" x="34" y="282" width="128" height="38"/>
    <text class="barcode-note" x="98" y="304" text-anchor="middle">BAR CODE</text>

    <!-- brand -->
    <text class="brand-name" x="388" y="100" text-anchor="middle">PLINTH</text>
    <text class="brand-flavor" x="388" y="134" text-anchor="middle">UNFLAVORED</text>

    <!-- spine -->
    <text class="oswald-thin fill-yellow" transform="translate(581 296) rotate(-90)" font-size="66" textLength="272" lengthAdjust="spacingAndGlyphs">PUREFORM</text>
    <rect class="fill-yellow" x="597" y="24" width="1.4" height="276"/>
    <text class="oswald-light fill-white" transform="translate(629 298) rotate(-90)" font-size="33" textLength="274" lengthAdjust="spacingAndGlyphs">100% WHEY PROTEIN</text>
    <text class="oswald-light fill-yellow" transform="translate(662 294) rotate(-90)" font-size="30" textLength="92" lengthAdjust="spacingAndGlyphs">40 SERVINGS</text>
    <rect class="fill-yellow" x="648" y="184" width="1.2" height="20"/>
    <text class="oswald-light fill-yellow" transform="translate(662 182) rotate(-90)" font-size="14" textLength="166" lengthAdjust="spacingAndGlyphs">50 Grams of Protein per serving</text>
    <text class="oswald-light fill-white" x="526" y="318" font-size="17" textLength="138" lengthAdjust="spacingAndGlyphs">Net WT. 3LB (1.36 KG)</text>
  </svg>

  <div class="abs intro-title">Pure Naked Protein</div>
  <p class="abs intro-copy">Lorem ipsum dolor sit amet, consectetuer adipiscing elit, sed diam nonummy nibh euismod tincidunt ut laoreet dolore magna aliquam erat volutpat. Ut wisi enim ad minim veniam,</p>

  <!-- nutrition -->
  <div class="abs facts">
    <h2>Nutrition Facts</h2>
    <div>Serving Size 3 Scoops (65g)</div>
    <div class="thick">Servings Per Container 40</div>
    <div class="thin"><b>Amount Per Serving</b></div>
    <div class="row thick"><b>Calories 230</b><span>Calories from Fat 10</span></div>
    <div class="row thin"><span></span><b>% Daily Value*</b></div>
    <div class="cols thick">
      <div>
        <div class="row thin"><b>Total Fat 1g</b><span>1%</span></div>
        <div class="row thin"><span>Saturated Fat 0.5g</span><span>3%</span></div>
        <div class="row thin"><span>Trans Fat 0g</span><span></span></div>
        <div class="row thin"><b>Cholesterol 5mg</b><span>2%</span></div>
        <div class="row"><b>Sodium 300mg</b><span>13%</span></div>
      </div>
      <div>
        <div class="row thin"><b>Potassium 700mg</b><span>20%</span></div>
        <div class="row thin"><b>Total Carbohydrate 3g</b><span>1%</span></div>
        <div class="row thin"><span>Dietary Fiber 0g</span><span>0%</span></div>
        <div class="row thin"><span>Sugars 2g</span><span></span></div>
        <div class="row"><b>Protein 50g</b><span>100%</span></div>
      </div>
    </div>
    <div class="grid thick">
      <span><i>Vitamin A</i>50%</span><span><i>Niacin</i>50%</span><span><i>Magnesium</i>50%</span>
      <span><i>Vitamin C</i>50%</span><span><i>Zinc</i>50%</span><span><i>Selenium</i>50%</span>
      <span><i>Calcium</i>8%</span><span><i>Folate</i>50%</span><span><i>Copper</i>50%</span>
      <span><i>Iron</i>6%</span><span><i>Biotin</i>50%</span><span><i>Chromium</i>50%</span>
    </div>
    <div>*Percent Daily Values are based on a 2,000 calorie diet.</div>
  </div>

  <p class="abs ingredients-side"><strong>Ingredients:</strong> Lorem ipsum dolor sit amet, consectetuer adipiscing elit, sed diam nonummy nibh euismod tincidunt ut laoreet dolore magna aliquam erat volutpat. Ut wisi enim ad minim veniam, quis nostrud exerci tation ullamcorper suscipit lobortis nisl ut aliquip ex ea commodo consequat. Duis autem vel eum iriure dolor in hendrerit in vulputate velit esse molestie consequat, vel illum dolore eu feugiat nulla facilisis at vero eros et accumsan et iusto odio dignissim qui blandit praesent luptatum zzril delenit augue duis dolore te feugait nulla facilisi.</p>

  <p class="abs info info-ingredients"><strong>Ingredients:</strong> Lorem ipsum dolor sit amet, consectetuer adipiscing elit, sed diam nonummy. nibh euismod tincidunt ut laoreet dolore magna aliquam erat volutpat. Ut wisi enim ad</p>
  <p class="abs info info-contains"><strong>Contains:</strong> Milk and Soy.</p>
  <p class="abs info info-maker"><strong>Manufactured for:</strong> Lorem ipsum dolor sit amet, consectetuer adipiscing elit, sed diam nibh euismod tincidunt ut laoreet dolore magna aliquam erat volutpat. Ut wisi enim ad</p>
  <p class="abs info lead info-storage">Contents sold by weight, not volume, keep in a cool, dry place.</p>
  <p class="abs info lead info-origin">Made in the USA- This product contains ingredients of international and domestic origin</p>

</div>
</body>
</html>
```